Business Card Design

Looking for business card designs for a new business. there will be two cards of the same design (both lots of information below in contact info). We would like the logo diagonally across the card with the information split above and below the logo similar to sketch. happy to look at similar alternatives
Please use same colours as in logo design

Industry/Entity Type

Business

Contact Information for Business Card

Gareth Mullins
mob - 0498 172 309
ph - 02 4839 2100
fax - 02 4839 2400
email - gaz@ridgelinetrusses.com.au
14 Calloway Road, Parrinda NSW 2340

Desmond Alcott
mob - 0426 918 753
ph - 02 4839 2100
fax - 02 4839 2400
email - desmond@ridgelinetrusses.com.au

```html
<!DOCTYPE html>
<html lang="en">
<head>
<meta charset="utf-8">
<title>Ridgeline Trusses — Business Cards</title>
<link href="https://fonts.googleapis.com/css2?family=Source+Sans+3:wght@400;600;700&display=swap" rel="stylesheet">
<style>
  :root {
    --teal: #0c7f7a;
    --ink: #111111;
    --paper: #ffffff;
    --backdrop: #e8e5e0;
    --text: #2b2b2b;
  }
  * { box-sizing: border-box; margin: 0; padding: 0; }
  html, body {
    width: 1145px;
    height: 1200px;
    overflow: hidden;
    background: var(--backdrop);
    font-family: "Source Sans 3", "Myriad Pro", Arial, sans-serif;
  }
  .canvas { position: relative; width: 1145px; height: 1200px; }

  /* Front card */
  .card-front {
    position: absolute;
    left: 172px; top: 39px;
    width: 940px; height: 537px;
    background: var(--paper);
    border: 1px solid #555;
    overflow: hidden;
  }
  .card-front .top-bar {
    position: absolute;
    left: 0; top: 0;
    width: 586px; height: 28px;
    background: var(--ink);
  }
  .brand {
    position: absolute;
    display: flex;
    align-items: center;
    gap: 16px;
    font-weight: 700;
    white-space: nowrap;
    letter-spacing: -0.5px;
  }
  .brand-mark { display: block; flex: none; }
  .card-front .brand {
    left: 28px; top: 70px;
    font-size: 66px;
    color: var(--ink);
  }
  .card-front .brand-mark { width: 40px; height: 40px; background: var(--teal); }

  .contact-list {
    position: absolute;
    right: 32px; top: 266px;
    list-style: none;
    text-align: right;
    font-size: 23px;
    color: var(--text);
    line-height: 36px;
  }
  .contact-list li {
    display: flex;
    justify-content: flex-end;
    align-items: center;
    gap: 6px;
  }
  .contact-list svg { width: 20px; height: 20px; fill: var(--teal); flex: none; }
  .address {
    position: absolute;
    right: 32px; top: 426px;
    font-size: 23px;
    line-height: 36px;
    color: var(--text);
    white-space: nowrap;
  }
  .name-band {
    position: absolute;
    right: 0; bottom: 0;
    width: 480px; height: 56px;
    background: var(--teal);
    color: var(--paper);
    font-weight: 700;
    font-size: 29px;
    text-align: right;
    padding-right: 38px;
    line-height: 56px;
  }

  /* Back card */
  .card-back {
    position: absolute;
    left: 28px; top: 623px;
    width: 942px; height: 537px;
    background: var(--ink);
  }
  .card-back .brand {
    left: 126px; top: 170px;
    font-size: 82px;
    color: var(--teal);
  }
  .card-back .brand-mark { width: 52px; height: 52px; background: var(--paper); }
  .website {
    position: absolute;
    left: 0; right: 0; top: 425px;
    text-align: center;
    color: var(--paper);
    font-size: 28px;
    letter-spacing: 2.5px;
  }
  .website strong { font-weight: 600; }
</style>
</head>
<body>
<div class="canvas">

  <section class="card-front">
    <div class="top-bar"></div>
    <div class="brand"><span class="brand-mark"></span>Ridgeline Trusses</div>

    <ul class="contact-list">
      <li>
        <svg viewBox="0 0 24 24" aria-hidden="true"><path d="M6.6 10.8a15 15 0 0 0 6.6 6.6l2.2-2.2c.3-.3.7-.4 1-.2 1.1.4 2.3.6 3.6.6.6 0 1 .4 1 1V20c0 .6-.4 1-1 1A17 17 0 0 1 3 4c0-.6.4-1 1-1h3.5c.6 0 1 .4 1 1 0 1.3.2 2.5.6 3.6.1.3 0 .7-.2 1z"/></svg>
        02 4839 2100
      </li>
      <li>
        <svg viewBox="0 0 24 24" aria-hidden="true"><path d="M7 1h10a2 2 0 0 1 2 2v18a2 2 0 0 1-2 2H7a2 2 0 0 1-2-2V3a2 2 0 0 1 2-2zm0 3v13h10V4zm5 15a1.3 1.3 0 1 0 0 2.6 1.3 1.3 0 0 0 0-2.6z"/></svg>
        0426 918 753
      </li>
      <li>
        <svg viewBox="0 0 24 24" aria-hidden="true"><path d="M6 2h10l2 2v5H6zM3 10h18a2 2 0 0 1 2 2v7a2 2 0 0 1-2 2H3a2 2 0 0 1-2-2v-7a2 2 0 0 1 2-2zm2 3v2h4v-2zm10 3a2 2 0 1 0 0 .1z"/></svg>
        02 4839 2400
      </li>
      <li>
        <svg viewBox="0 0 24 24" aria-hidden="true"><path d="M2 9l10-6 10 6v11a1 1 0 0 1-1 1H3a1 1 0 0 1-1-1zm2 1.2V19h16v-8.8l-8 5z"/></svg>
        desmond@ridgelinetrusses.com.au
      </li>
    </ul>

    <p class="address">14 Calloway Road, Parrinda NSW 2340</p>
    <div class="name-band">Desmond Alcott</div>
  </section>

  <section class="card-back">
    <div class="brand"><span class="brand-mark"></span>Ridgeline Trusses</div>
    <p class="website">www.<strong>ridgelinetrusses</strong>.com.au</p>
  </section>

</div>
</body>
</html>
```